Stylise 5 diagrams to feature on webpage

We need existing diagrams recreated in a stylized format to go on our web page.

We will provide all required drafts and are after a style/design set which will work with our brand identity, target market and existing website.

Company Background
- We are a provider of data, software and services which blue chip companies use to shape their customer experience. ie very high tier companies, so our audience are of a high calibre.

What we want to present is clarity of thought, expertise and authority (ie we deal in data so a certain amount of conservatism is required to inspire trust in our data). However we dont want this to appear old and 'stuffy'. We want to present as the savvy partner who know their stuff but at the same time are modern and innovative and fresh.
So I am imagining crisp, clean, slick and innovative.

Potential for ongoing work
This project will have a number of images to recreate initially. However we will need an ongoing service/provider which can duplicate the style.
Other pieces may include designing PPT templates, presentations, reports, web, brochures etc

Website that the diagrams will live within.
http://new.quillmarkdata.com.au/ this is the start of the new web page. the images will sit inside the content and will need to 'balance' the currently high text to image ratio and work with the existing logo and style.
Please don't let the existing website limit your creativity or inspiration - we are open to improving our design elements :) What I do want to retain in alignment with the website is simplicity and 'crisp', ie use of clean fonts and sharp colours.

Attached are our existing brand guides. Again, please observe these loosely but feel free to offer up any improvements. The key here is that the Aubergine key colour is respected.

NOTE: Both attached files are the same but in different formats as some were having troubles opening.

Target Market(s)

Target Market(s)
- Executives of large blue chip companies (think airlines, telcos, etc).
- Consulting firms (think Hollingford Brackett, RTVW, Garrowby)

Industry/Entity Type

Software

Requirements
Must have
• Must haves
- PSD editable format for text, graphics, all elements
- the diagrams required must look to be of the same design 'family'. Once we establish this style we can progress to develop all the required diagrams and in future create a rship where we develop additional company collateral

```html
<!DOCTYPE html>
<html lang="en">
<head>
<meta charset="utf-8">
<title>Customer Experience Programme Cycle</title>
<link rel="stylesheet" href="https://fonts.googleapis.com/css2?family=PT+Sans:wght@400;700&display=swap">
<style>
  :root {
    --aubergine: #a3175c;
    --aubergine-light: #c8509a;
    --grey-dark: #8a8a8a;
    --grey-light: #d2d2d2;
    --row-pink: #f8e8ef;
    --row-grey: #efefef;
    --ink: #1f1f1f;
    --white: #ffffff;
  }
  * { box-sizing: border-box; margin: 0; padding: 0; }
  html, body { width: 1200px; height: 1044px; overflow: hidden; background: var(--white); }
  body { font-family: "PT Sans", Arial, sans-serif; color: var(--ink); position: relative; }

  .cycle { position: absolute; left: 13px; top: 14px; width: 1158px; }
  .stage {
    position: relative; height: 200px; margin-bottom: 6px;
    border-radius: 12px; overflow: hidden;
  }
  .stage:last-child { margin-bottom: 0; }
  .stage--brand { background: var(--row-pink); }
  .stage--neutral { background: var(--row-grey); }

  .stage__label {
    position: absolute; left: 0; top: 0; bottom: 0; width: 77px;
    border-radius: 12px;
    display: flex; align-items: center; justify-content: center;
  }
  .stage--brand .stage__label { background: linear-gradient(90deg, var(--aubergine), var(--aubergine-light)); }
  .stage--neutral .stage__label { background: linear-gradient(90deg, var(--grey-dark), var(--grey-light)); }
  .stage__label span {
    transform: rotate(-90deg); white-space: nowrap;
    color: var(--white); font-weight: 700; font-size: 27px;
  }

  .step {
    position: absolute; top: 50%; transform: translateY(-50%);
    width: 170px; height: 121px; border-radius: 10px;
    display: flex; align-items: center; justify-content: center; text-align: center;
    font-weight: 700; font-size: 24px; line-height: 30px;
    box-shadow: 2px 3px 5px rgba(0,0,0,0.22);
  }
  .step--brand { background: linear-gradient(90deg, var(--aubergine), var(--aubergine-light)); color: var(--white); }
  .step--neutral { background: linear-gradient(90deg, var(--grey-dark), var(--grey-light)); color: var(--ink); }

  .note {
    position: absolute; top: 50%; transform: translate(-50%, -50%);
    text-align: center; font-size: 24px; line-height: 33px; white-space: nowrap;
  }
  .note li { list-style: none; }
  .note li::before { content: "• "; }
</style>
</head>
<body>
<main class="cycle">

  <section class="stage stage--brand">
    <div class="stage__label"><span>Establish</span></div>
    <div class="step step--brand" style="left:110px;">Define<br>Customer<br>“Cycle”</div>
    <ul class="note" style="left:715px;">
      <li>Moments of Truth</li>
      <li>Interaction Points</li>
      <li>What is Important to customers (SERVQUAL approach)</li>
    </ul>
  </section>

  <section class="stage stage--neutral">
    <div class="stage__label"><span>Listen</span></div>
    <p class="note" style="left:197px;">Project<br>Governance</p>
    <div class="step step--neutral" style="left:282px;">Establish<br>Listening<br>Posts</div>
    <ul class="note" style="left:822px;">
      <li>Key Drivers derived - process &amp; emotion</li>
      <li>Questionnaire design</li>
      <li>Operations - customer selection, data integration,</li>
      <li style="list-style:none;" class="plain">channel selection, operational procedures etc.</li>
      <li>Reporting</li>
    </ul>
  </section>

  <section class="stage stage--brand">
    <div class="stage__label"><span>Act</span></div>
    <p class="note" style="left:273px;">Portal Design &amp;<br>Implementation</p>
    <div class="step step--brand" style="left:449px;">Action<br>Processes</div>
    <ul class="note" style="left:892px;">
      <li>Staff selection</li>
      <li>Action guidelines</li>
      <li>Training</li>
      <li>Reporting</li>
    </ul>
  </section>

  <section class="stage stage--neutral">
    <div class="stage__label"><span>Discover</span></div>
    <p class="note" style="left:363px;">Pulse Implementation,<br>data Integration</p>
    <div class="step step--neutral" style="left:606px;">Discover<br>Customer<br>Issues</div>
    <ul class="note" style="left:989px;">
      <li>Unstructured &amp; Structured data</li>
      <li>By Interaction Point</li>
      <li>Cross functional review</li>
      <li>Identify high priority MOT/</li>
      <li class="plain">Interaction Point</li>
    </ul>
  </section>

  <section class="stage stage--brand">
    <div class="stage__label"><span>Improve</span></div>
    <ul class="note" style="left:388px;">
      <li>Physical Process - Touchpoint Mapping,</li>
      <li class="plain">Gap &amp; root cause analysis</li>
      <li>Emotional Drivers - Moment Mapping,</li>
      <li class="plain">Gap &amp; root cause analysis</li>
      <li>Improvement Plan</li>
    </ul>
    <div class="step step--brand" style="left:773px;">Improve<br>the<br>experience</div>
    <p class="note" style="left:1048px;">PIR<br>Go to “Listen”</p>
  </section>

</main>
<style>
  .note li.plain::before { content: ""; }
</style>
</body>
</html>
```